Health care technology software systems

We have a solid logo. We have company colors that will need to be used as well. We just need a great business card design. We sell to health plans but want to be modern
Updates

Need extra days to review

Target Market(s)

Health technology sector selling into Health Plans

Industry/Entity Type

Health Care Technology

Contact Information for Business Card

Name, title, address, phone number, email

Requirements
Must have
• Use of Kembrata corporate colors - Uploaded w/ our logos

```html
<!DOCTYPE html>
<html lang="en">
<head>
<meta charset="utf-8">
<title>Kembrata Business Card</title>
<link rel="stylesheet" href="https://fonts.googleapis.com/css2?family=Poppins:wght@300;400;500;600&display=swap">
<style>
  :root {
    --backdrop: #ababab;
    --card-light: #ececec;
    --card-dark: #101114;
    --ink: #2b2b2b;
    --brand-navy: #3a5cab;
    --brand-sky: #1aa0dc;
    --brand-green: #80bd3a;
    --white: #ffffff;
  }
  * { margin: 0; padding: 0; box-sizing: border-box; }
  html, body {
    width: 1127px; height: 1200px; overflow: hidden;
    background: var(--backdrop);
    font-family: "Poppins", sans-serif;
  }
  .stage { position: relative; width: 1127px; height: 1200px; }
  .card {
    position: absolute; left: 323px;
    width: 600px; height: 346px;
    transform: scale(0.857); transform-origin: top left;
    overflow: hidden;
  }
  .card--front { top: 263px; background: var(--card-light); }
  .card--back { top: 642px; background: var(--card-dark); }

  .accent-stripes { position: absolute; top: 0; right: 0; }

  .front-mark {
    position: absolute; left: 40px; top: 60px; width: 260px;
    display: flex; flex-direction: column; align-items: center; gap: 18px;
  }
  .front-mark__dot {
    width: 150px; height: 150px; border-radius: 50%;
    background: var(--brand-sky);
  }
  .front-mark__name {
    font-size: 26px; font-weight: 500; color: var(--brand-navy);
  }

  .holder { position: absolute; left: 327px; top: 70px; color: var(--ink); }
  .holder__name { font-size: 22px; font-weight: 600; line-height: 1.2; }
  .holder__title { font-size: 17px; font-weight: 400; letter-spacing: 1.5px; line-height: 1.3; }

  .contact-icons { position: absolute; left: 332px; top: 159px; display: flex; gap: 19px; }
  .contact-icon {
    width: 33px; height: 33px; border-radius: 4px;
    display: flex; align-items: center; justify-content: center;
  }
  .contact-icon--phone { background: var(--brand-navy); }
  .contact-icon--mail { background: var(--brand-green); }
  .contact-icon--web { background: var(--brand-sky); }

  .divider {
    position: absolute; left: 326px; top: 213px;
    width: 232px; height: 2px; background: var(--ink);
  }
  .contact-list {
    position: absolute; left: 327px; top: 230px;
    list-style: none; color: var(--ink);
    font-size: 14.5px; letter-spacing: 0.8px; line-height: 21.5px;
  }

  .back-mark {
    position: absolute; inset: 0;
    display: flex; align-items: center; justify-content: center; gap: 30px;
  }
  .back-mark__dot {
    width: 74px; height: 74px; border-radius: 50%;
    background: var(--brand-sky);
  }
  .back-mark__name {
    font-size: 66px; font-weight: 300; color: var(--white);
    letter-spacing: 1px; line-height: 1;
  }
</style>
</head>
<body>
<main class="stage">
  <section class="card card--front">
    <svg class="accent-stripes" width="300" height="21" viewBox="0 0 300 21">
      <polygon points="0,0 115,0 135,21 20,21" fill="var(--brand-sky)"/>
      <polygon points="115,0 230,0 250,21 135,21" fill="var(--brand-green)"/>
      <polygon points="230,0 300,0 300,21 250,21" fill="var(--brand-navy)"/>
    </svg>

    <div class="front-mark">
      <span class="front-mark__dot"></span>
      <span class="front-mark__name">Kembrata</span>
    </div>

    <div class="holder">
      <p class="holder__name">MARCUS ELLERY</p>
      <p class="holder__title">OWNER</p>
    </div>

    <div class="contact-icons">
      <span class="contact-icon contact-icon--phone">
        <svg width="20" height="20" viewBox="0 0 24 24"><path fill="#fff" d="M6.6 10.8a15 15 0 0 0 6.6 6.6l2.2-2.2c.3-.3.7-.4 1-.2 1.1.4 2.3.6 3.6.6.6 0 1 .4 1 1V20c0 .6-.4 1-1 1A17 17 0 0 1 3 4c0-.6.4-1 1-1h3.5c.6 0 1 .4 1 1 0 1.3.2 2.5.6 3.6.1.3 0 .7-.2 1z"/></svg>
      </span>
      <span class="contact-icon contact-icon--mail">
        <svg width="22" height="16" viewBox="0 0 22 16"><rect x="1" y="1" width="20" height="14" fill="none" stroke="#fff" stroke-width="1.6"/><polyline points="1,1 11,9 21,1" fill="none" stroke="#fff" stroke-width="1.6"/></svg>
      </span>
      <span class="contact-icon contact-icon--web">
        <svg width="22" height="22" viewBox="0 0 22 22" fill="none" stroke="#fff" stroke-width="1.4"><circle cx="11" cy="11" r="9"/><ellipse cx="11" cy="11" rx="4" ry="9"/><line x1="2" y1="11" x2="20" y2="11"/><path d="M3.5 6.5h15M3.5 15.5h15"/></svg>
      </span>
    </div>

    <div class="divider"></div>

    <ul class="contact-list">
      <li>123 456 7890</li>
      <li>email@domainname.com</li>
      <li>www.websitehere.com</li>
    </ul>
  </section>

  <section class="card card--back">
    <div class="back-mark">
      <span class="back-mark__dot"></span>
      <span class="back-mark__name">kembrata</span>
    </div>
  </section>
</main>
</body>
</html>
```